Seven Rising Steps - Site signage graphic

I need a large board creating to show our Seven Bright Paths plan.

I have added a previous version of this called Seven Bold Moves as well as the draft (AI) version of Seven Rising Steps and our new PowerPoint as an example of branding .

Target Market(s)

Colleagues and visitors to site

Industry/Entity Type

Food manufacturing

Font styles to use
Other font styles liked:
• Raleway Medium

Requirements
Must have
• Clear and all text as per AI mock up

```html
<!DOCTYPE html>
<html lang="en">
<head>
<meta charset="utf-8">
<title>Brookmead Foods – Seven Bright Paths site board</title>
<link href="https://fonts.googleapis.com/css2?family=Anton&family=Raleway:wght@500;700;800&family=Lora:wght@400&family=Caveat+Brush&display=swap" rel="stylesheet">
<style>
:root{
  --green:#0b4a2e;
  --orange:#e0661c;
  --yellow:#e8a21f;
  --cream:#ece4d4;
  --white:#ffffff;
  --page:#d9d4cb;
}
*{box-sizing:border-box;margin:0;padding:0}
html,body{width:1200px;height:765px;overflow:hidden;background:var(--page)}
.board{position:absolute;left:20px;top:57px;width:1160px;height:651px;background:var(--cream);overflow:hidden}
.brand{position:absolute;left:33px;top:14px;display:flex;align-items:center;gap:6px;font:800 17px/1 'Raleway',sans-serif;color:var(--green);letter-spacing:.3px}
.brand-dot{width:10px;height:10px;border-radius:50%;background:var(--orange)}
.headline{position:absolute;left:33px;top:80px;font:400 37px/37px 'Anton',sans-serif;color:var(--green);text-transform:uppercase}
.plan-name{position:absolute;left:33px;top:236px;width:252px}
.plan-name .lead{font:400 50px/52px 'Anton',sans-serif;color:var(--orange);text-transform:uppercase}
.plan-name .bar{display:inline-block;background:var(--green);color:var(--white);font:400 40px/50px 'Anton',sans-serif;padding:0 14px 0 8px;border-radius:0 12px 0 0;text-transform:uppercase}
.rule{position:absolute;left:98px;top:356px;width:148px;height:2px;background:var(--orange)}
.heritage{position:absolute;left:36px;top:366px;font:400 21px/26px 'Lora',serif;color:var(--green)}
.future{position:absolute;left:36px;top:392px;font:400 23px/28px 'Caveat Brush',cursive;color:var(--yellow)}
.farm-scene{position:absolute;left:33px;top:424px;width:252px;height:128px;background:linear-gradient(180deg,#e6ddcb,#cfd6c4);border-radius:2px}
.label{position:absolute;left:37px;background:var(--green);font:500 12.5px/18px 'Raleway',sans-serif;padding:0 10px;text-transform:uppercase}
.label.one{top:556px;color:var(--white)}
.label.two{top:576px;color:var(--yellow);width:247px}
.footer-line{position:absolute;left:37px;top:600px;font:400 15px/20px 'Anton',sans-serif;color:var(--green);text-transform:uppercase;letter-spacing:-.1px}
.sign-off{position:absolute;left:78px;top:620px;font:400 20px/24px 'Caveat Brush',cursive;color:var(--orange)}
.sign-off span{text-decoration:underline;text-decoration-thickness:2px}
.priorities{position:absolute;left:300px;top:9px;width:800px}
.priority{position:relative;height:122px;margin-bottom:5px;display:flex;align-items:center}
.num{width:75px;text-align:center;font:400 118px/1 'Anton',sans-serif}
.band{position:absolute;left:75px;top:0;width:740px;height:122px;border-radius:16px 0 0 16px;display:flex;align-items:flex-start}
.priority.green .band{background:var(--green)}
.priority.orange .band{background:var(--orange)}
.priority.green .num{color:var(--green)}
.priority.orange .num{color:var(--orange)}
.icon{margin:20px 0 0 48px;width:97px;height:97px;flex:none}
.icon svg{width:97px;height:97px;margin-top:-8px}
.copy{margin:12px 0 0 31px;width:450px}
.title{font:400 29px/34px 'Anton',sans-serif;text-transform:uppercase;color:var(--orange)}
.priority.orange .title{color:var(--green)}
.sub{font:700 12.5px/16px 'Raleway',sans-serif;text-transform:uppercase;color:var(--yellow);margin-top:2px}
.priority.orange .sub{color:#f4b23a}
.body{font:500 12px/15px 'Raleway',sans-serif;color:var(--white);margin-top:3px}
.burst{position:absolute;right:0;top:0;width:170px;height:651px}
</style>
</head>
<body>
<main class="board">
  <div class="brand"><span class="brand-dot"></span>Brookmead Foods</div>

  <h1 class="headline">From<br>Cheesemakers<br>to<br>Changemakers :</h1>

  <div class="plan-name">
    <div class="lead">Seven</div>
    <div class="bar">Bright Paths</div>
  </div>

  <div class="rule"></div>
  <p class="heritage">Proud of our heritage.</p>
  <p class="future">Focused on our future.</p>

  <div class="farm-scene" role="img" aria-label="Line illustration of a farmhouse, barn and grazing dairy cow in green ink"></div>

  <div class="label one">From farm to fork.</div>
  <div class="label two">We're shaping the industry.</div>
  <p class="footer-line">One business. One purpose. Five priorities.</p>
  <p class="sign-off">Let's thrive <span>together</span>.</p>

  <section class="priorities">
    <article class="priority green">
      <div class="num">1</div>
      <div class="band">
        <div class="icon"><svg viewBox="0 0 100 100"><circle cx="50" cy="50" r="46" fill="none" stroke="#e8a21f" stroke-width="3"/><g fill="none" stroke="#fff" stroke-width="3"><circle cx="34" cy="30" r="6"/><circle cx="50" cy="27" r="6"/><circle cx="66" cy="30" r="6"/><path d="M24 48c0-8 5-12 10-12s10 4 10 12M40 46c0-8 5-12 10-12s10 4 10 12M56 48c0-8 5-12 10-12s10 4 10 12"/></g><path d="M30 76c6-18 22-26 42-24-4 18-22 28-42 24z" fill="#2f8a3e" stroke="#9bd16a" stroke-width="2"/><path d="M32 74c10-8 20-14 34-18" stroke="#9bd16a" stroke-width="2" fill="none"/></svg></div>
        <div class="copy">
          <h2 class="title">People, Places &amp; Products</h2>
          <p class="sub">We do things the right way</p>
          <p class="body">Our success starts with great people, strong communities and quality milk. We are committed to producing food responsibly, supporting our farming partners and creating opportunities for future generations.</p>
        </div>
      </div>
    </article>

    <article class="priority orange">
      <div class="num">2</div>
      <div class="band">
        <div class="icon"><svg viewBox="0 0 100 100"><circle cx="50" cy="50" r="46" fill="none" stroke="#0b4a2e" stroke-width="3"/><g stroke="#fff" stroke-width="2.5" fill="none"><rect x="36" y="36" width="28" height="28" rx="3"/><path d="M44 36V24M56 36V24M44 64v12M56 64v12M36 44H24M36 56H24M64 44h12M64 56h12"/><circle cx="44" cy="21" r="3"/><circle cx="56" cy="21" r="3"/><circle cx="44" cy="79" r="3"/><circle cx="56" cy="79" r="3"/><circle cx="21" cy="44" r="3"/><circle cx="21" cy="56" r="3"/><circle cx="79" cy="44" r="3"/><circle cx="79" cy="56" r="3"/></g><rect x="43" y="48" width="14" height="11" rx="1.5" fill="none" stroke="#f4b23a" stroke-width="2.5"/><path d="M46 48v-4a4 4 0 0 1 8 0v4" fill="none" stroke="#f4b23a" stroke-width="2.5"/></svg></div>
        <div class="copy">
          <h2 class="title">Cyber Security</h2>
          <p class="sub">Protecting what matters</p>
          <p class="body">Every colleague plays a role in keeping our information, systems and customers safe. Strong cyber security protects our business today and supports our future growth.</p>
        </div>
      </div>
    </article>

    <article class="priority green">
      <div class="num">3</div>
      <div class="band">
        <div class="icon"><svg viewBox="0 0 100 100"><circle cx="50" cy="50" r="46" fill="none" stroke="#e8a21f" stroke-width="3"/><path d="M38 56l-8 20 8-3 4 7 6-18M62 56l8 20-8-3-4 7-6-18" fill="#fff"/><circle cx="50" cy="42" r="20" fill="#fff"/><circle cx="50" cy="42" r="13" fill="#e0661c"/><path d="M44 42l4 4 8-8" fill="none" stroke="#0b4a2e" stroke-width="3"/></svg></div>
        <div class="copy">
          <h2 class="title">Quality &amp; Continuous Improvement</h2>
          <p class="sub">Be the best at what we do</p>
          <p class="body">Quality and food safety are at the heart of everything we do. By continually improving our processes, reducing waste and learning every day, we deliver products our customers can trust.</p>
        </div>
      </div>
    </article>

    <article class="priority orange">
      <div class="num">4</div>
      <div class="band">
        <div class="icon"><svg viewBox="0 0 100 100"><circle cx="50" cy="50" r="46" fill="none" stroke="#0b4a2e" stroke-width="3"/><circle cx="50" cy="50" r="32" fill="none" stroke="#fff" stroke-width="2.5"/><path d="M50 12v10M50 78v10M12 50h10M78 50h10" stroke="#fff" stroke-width="2.5"/><circle cx="50" cy="38" r="6" fill="#f4b23a"/><rect x="42" y="46" width="16" height="16" rx="3" fill="#f4b23a"/><circle cx="36" cy="44" r="4.5" fill="#fff"/><rect x="30" y="50" width="12" height="12" rx="2" fill="#fff"/><circle cx="64" cy="44" r="4.5" fill="#fff"/><rect x="58" y="50" width="12" height="12" rx="2" fill="#fff"/></svg></div>
        <div class="copy">
          <h2 class="title">Customer Focus</h2>
          <p class="sub">Build trust. Create value. For the long term.</p>
          <p class="body">We build strong, long-term relationships based on trust by understanding our customers' needs and working together to deliver outstanding value.</p>
        </div>
      </div>
    </article>

    <article class="priority green">
      <div class="num">5</div>
      <div class="band">
        <div class="icon"><svg viewBox="0 0 100 100"><circle cx="50" cy="50" r="46" fill="none" stroke="#e8a21f" stroke-width="3"/><g stroke="#fff" stroke-width="2.5"><path d="M50 14v7M26 26l5 5M74 26l-5 5M16 50h7M77 50h7M28 72l5-4"/></g><path d="M50 30a16 16 0 0 0-9 29v8h9z" fill="#fff"/><path d="M50 30a16 16 0 0 1 9 29v8h-9z" fill="#e8a21f"/><rect x="42" y="70" width="16" height="3" fill="#fff"/><rect x="44" y="75" width="12" height="3" fill="#fff"/></svg></div>
        <div class="copy">
          <h2 class="title">Transformation &amp; Innovation</h2>
          <p class="sub">Shaping tomorrow, today</p>
          <p class="body">We challenge ourselves to think differently, embrace change and never stand still. Through innovation, collaboration and continuous improvement, we will build a stronger, smarter and more sustainable Brookmead Foods for the future.</p>
        </div>
      </div>
    </article>
  </section>

  <svg class="burst" viewBox="990 0 170 651" aria-hidden="true">
    <polygon points="1081,0 1160,0 1160,651 1020,651 1039,520" fill="#0b4a2e"/>
    <polygon points="1081,0 1160,42 1160,309 1010,520" fill="#e8a21f"/>
    <polygon points="1040,650 1160,560 1160,600" fill="#e0661c"/>
    <polygon points="1035,560 1160,540 1160,555" fill="#e0661c"/>
    <polygon points="1040,450 1160,370 1160,470 1080,420" fill="#e0661c"/>
    <polygon points="1080,470 1160,450 1160,470" fill="#e8a21f"/>
    <polygon points="1030,500 1160,520 1160,535" fill="#e8a21f"/>
    <polygon points="1060,610 1160,640 1160,651 1090,651" fill="#e0661c"/>
  </svg>
</main>
</body>
</html>
```